Educational clinic needs a new webpage design

I have a relatively new website but I am unhappy with the design. I was hoping the look of it would more match my logo, brochures, business cards, and postcards. The content is good and it's already mobile ready. The designer used square space, which I would like to keep if possible. My website is www.willowgatestudio.com

Target Market(s)

Parents of school age children

Industry/Entity Type

Education

Number of Pages Required

5+ page

Requirements
Must have
• Pictures must depict the diversity of our students. We service all ages, from preschool through college and our students come from varying races.
Should not have
• I try to avoid the word "tutoring" because what we do is so much more. I like the tag line of "results that go beyond traditional tutoring"

```html
<!DOCTYPE html>
<html lang="en">
<head>
<meta charset="utf-8">
<title>Willowgate Studio – Contact form</title>
<link rel="stylesheet" href="https://fonts.googleapis.com/css2?family=Arimo:wght@400;700&family=Merriweather:ital,wght@1,900&display=swap">
<style>
  :root {
    --purple: #6f2c91;
    --green: #8dc63f;
    --header-grey: #d9d9d9;
    --page-light: #f1f1f1;
    --ink: #333333;
    --field-border: #b9b9b9;
    --white: #ffffff;
    --muted: #555555;
  }
  * { box-sizing: border-box; margin: 0; padding: 0; }
  html, body { width: 1050px; height: 1200px; overflow: hidden; }
  body {
    position: relative;
    font-family: "Arimo", Arial, sans-serif;
    background: var(--page-light);
    color: var(--ink);
  }

  /* Background site page, softened behind the dialog */
  .site-page {
    position: absolute; inset: 0;
    filter: blur(2.5px);
    opacity: .9;
  }
  .site-header {
    position: absolute; left: 0; top: 0; width: 1050px; height: 148px;
    background: var(--header-grey);
  }
  .brand {
    position: absolute; left: 14px; top: 34px;
    display: flex; align-items: center; gap: 14px;
  }
  .brand-mark { width: 70px; height: 70px; border-radius: 50%; background: var(--purple); opacity: .8; }
  .brand-name { font-weight: 700; font-size: 38px; color: var(--purple); }
  .phone-pill {
    position: absolute; left: 870px; top: 50px; width: 200px; height: 68px;
    background: var(--green); border-radius: 8px 0 0 8px;
    font-weight: 700; font-size: 36px; color: #7a4a9a; letter-spacing: 2px;
    padding: 12px 0 0 18px;
  }
  .main-nav {
    position: absolute; left: 0; top: 148px; width: 1050px; height: 78px;
    background: var(--purple);
  }
  .nav-item {
    position: absolute; top: 24px;
    font-weight: 700; font-size: 24px; color: var(--white); letter-spacing: 1px;
  }
  .hero {
    position: absolute; left: 0; top: 226px; width: 1050px; height: 694px;
    background: linear-gradient(135deg, #c28ca8 0%, #a86d92 40%, #b98aa6 70%, #9c6a8c 100%);
  }
  .hero-line {
    position: absolute; top: 226px;
    font-family: "Merriweather", Georgia, serif; font-style: italic; font-weight: 900;
    font-size: 52px; color: var(--white);
  }
  .features {
    position: absolute; left: 0; top: 920px; width: 1050px; height: 280px;
    background: var(--page-light);
  }
  .feature { position: absolute; top: 24px; width: 260px; text-align: center; }
  .feature-icon { width: 56px; height: 56px; margin: 0 auto 18px; border-radius: 8px; background: #c9a98a; }
  .feature-title { font-size: 24px; color: #666; letter-spacing: .5px; margin-bottom: 8px; }
  .feature-text { font-size: 12px; line-height: 20px; color: #777; }
  .see-more {
    display: inline-block; width: 144px; height: 30px; margin-top: 14px;
    font-weight: 700; font-size: 18px; line-height: 30px; color: var(--white);
    letter-spacing: 1px; background: var(--purple);
  }
  .see-more--green { background: var(--green); }
  .pointer { position: absolute; left: 562px; top: 1140px; }

  /* Contact dialog */
  .contact-dialog {
    position: absolute; left: 165px; top: 46px; width: 720px; height: 1049px;
    background: var(--white); border-radius: 13px;
    box-shadow: 0 0 22px rgba(120, 120, 40, .55);
  }
  .dialog-title {
    position: absolute; left: 37px; top: 30px;
    font-weight: 700; font-size: 27px; letter-spacing: .8px; color: var(--ink);
  }
  .close-button { position: absolute; left: 627px; top: 36px; width: 52px; height: 52px; }
  .field-label {
    position: absolute; font-weight: 700; font-size: 18px; letter-spacing: .6px; color: var(--ink);
  }
  .field-input {
    position: absolute; width: 644px; height: 66px;
    border: 1.5px solid var(--field-border); border-radius: 3px; background: var(--white);
  }
  .field-input--message { height: 249px; }
  .send-button {
    position: absolute; left: 534px; top: 959px; width: 150px; height: 67px;
    background: var(--purple); border-radius: 12px;
    color: var(--white); font-size: 37px; text-align: center; line-height: 67px;
  }
</style>
</head>
<body>
  <div class="site-page" aria-hidden="true">
    <header class="site-header">
      <div class="brand">
        <span class="brand-mark"></span>
        <span class="brand-name">Willowgate Studio</span>
      </div>
      <div class="phone-pill">555-0142</div>
    </header>
    <nav class="main-nav">
      <span class="nav-item" style="left:0">HOME</span>
      <span class="nav-item" style="left:160px">SERVICES</span>
      <span class="nav-item" style="left:884px">ENTS</span>
    </nav>
    <div class="hero" role="img" aria-label="Photo of a student's desk with books, a tablet and study supplies in soft purple tones"></div>
    <span class="hero-line" style="left:6px; top:452px">that</span>
    <span class="hero-line" style="left:884px; top:452px">l Tuto</span>
    <section class="features">
      <div class="feature" style="left:-10px">
        <div class="feature-icon" role="img" aria-label="Graduate illustration"></div>
        <div class="feature-title">WHAT WE DO</div>
        <p class="feature-text">Since 2004, we have been helping<br>families with their education goals.<br>We are more than passionate ...</p>
        <span class="see-more">see more</span>
      </div>
      <div class="feature" style="left:476px">
        <div class="feature-icon" role="img" aria-label="Student illustration"></div>
        <div class="feature-title">WHY US</div>
        <p class="feature-text">There are many reasons why<br>our approach works so well and<br>a student may not be doing well in ...</p>
        <span class="see-more see-more--green">see more</span>
      </div>
      <div class="feature" style="left:880px">
        <div class="feature-icon" role="img" aria-label="Books illustration"></div>
        <div class="feature-title">EXAM PREP</div>
        <p class="feature-text">More than two million students<br>take entrance tests each year hoping to<br>be accepted into their college</p>
        <span class="see-more">see more</span>
      </div>
    </section>
    <svg class="pointer" width="40" height="52" viewBox="0 0 40 52">
      <path d="M12 4 v26 l-5 -5 q-5 -3 -3 3 l10 16 h18 l4 -14 v-10 q0 -4 -4 -3 v-3 q0 -4 -4 -3 v-1 q0 -4 -4 -3 v-3 q0 -4 -4 -3 v-8 q0 -5 -5 0 z" fill="#fff" stroke="#222" stroke-width="2"/>
    </svg>
  </div>

  <section class="contact-dialog" aria-label="Contact form">
    <h1 class="dialog-title">Contact form</h1>
    <svg class="close-button" viewBox="0 0 52 52" aria-label="Close">
      <path d="M5 5 L47 47 M47 5 L5 47" stroke="#9a9a2a" stroke-width="8" stroke-linecap="round" transform="translate(1.5,1.5)"/>
      <path d="M5 5 L47 47 M47 5 L5 47" stroke="#444" stroke-width="8" stroke-linecap="round"/>
    </svg>

    <label class="field-label" style="left:35px; top:89px">First Name*</label>
    <div class="field-input" style="left:38px; top:128px"></div>

    <label class="field-label" style="left:35px; top:232px">Last Name*</label>
    <div class="field-input" style="left:38px; top:271px"></div>

    <label class="field-label" style="left:37px; top:354px">Email Address*</label>
    <div class="field-input" style="left:40px; top:393px"></div>

    <label class="field-label" style="left:37px; top:496px">Subject*</label>
    <div class="field-input" style="left:40px; top:536px"></div>

    <label class="field-label" style="left:34px; top:639px">Message*</label>
    <div class="field-input field-input--message" style="left:37px; top:679px"></div>

    <div class="send-button">Send</div>
  </section>
</body>
</html>
```